Hernia Mesh Lawsuit - Banner & Creatives

Looking for design of ad banners and email creative for my Hernia Mesh Lawsuit website. Call to action based email focused on conveying brand, messaging of "have you had surgery using a surgical mesh, possibly for a hernia or a C-section? You may be eligible to join a surgical mesh class action lawsuit " and "ACT NOW: Check Your Eligibility Now." Call to action of 'Get Your Free Evaluation' or 'Fast, Free, No Obligation Evaluation'. Can use any messaging and images from the current website https://www.trelloviankase.com/pelvicweave/see-whether-you-qualify/ Please focus on imaging that matches the site. The final Ad Banners must be delivered in both JPG and PSD file formats. Ad Banners must follow OWD standards. The final Email creative must be done in repsonsive HTML as well as text for easy use and include Email Opt Out link etc. <br/>We need Ad Banners in the following sizes.<br/><br/>• 728x90 Leaderboard<br/>• 300x250 Inline Rectangle<br/>• 320x50 Mobile<br/>Target Market(s)<br/><br/>NATIONAL INJURY LAWSUIT - Have you or a loved one had surgery using a surgical mesh, possibly for a hernia or a C-section? You may be eligible to join a surgical mesh class action lawsuit if you had another surgery to remove the mesh or if you suffered any side effects, including: Bleeding Bowel obstruction Fluid buildup (seromas) Infection Mesh migration Nerve damage Pain To qualify, the surgical mesh can be of any type, including Vela-Fin, D-LARTM, Marvento’s LatrobandTM or any other brand.<br/>Industry/Entity Type<br/><br/>Lawyer<br/>Coding<br/><br/>Coded - Design and coding required<br/>Number of Pages Required<br/><br/>1 page<br/>Font styles to use<br/>Sans Serif<br/>Look and feel<br/><br/>Each slider illustrates characteristics of the customer's brand and the style your logo design should communicate.<br/>Elegant<br/>Bold<br/>Playful<br/>Serious<br/>Traditional<br/>Modern<br/>Personable<br/>Professional<br/>Feminine<br/>Masculine<br/>Colorful<br/>Conservative<br/>Economical<br/>Upmarket<br/><br/>Requirements<br/>Must have<br/><br/>* Call to action ad banners and Email creative.<br/>* Ad Banners in the 3 sizes noted in the project description.<br/>* Email creative must also be coded in responsive HTML.<br/>* The design must match the website https://harbor-lanternpage.com/<br/><br/>Nice to have<br/><br/>* Strong call to action<br/><br/>Should not have<br/><br/>* Should not be cookie cutter. Stick to simple yet official looking.

Target Market(s)

People who had another surgery to remove the mesh or if you suffered any side effects, including:

Bleeding
Bowel obstruction
Fluid buildup (seromas)
Infection

Mesh migration
Nerve damage
Pain

To qualify, the surgical mesh can be of any type, including Vela-Fin, D-LARTM, Marvento’s LatrobandTM or any other brand.

Industry/Entity Type

Legal

Font styles to use
Serif

Colors

Designer to choose colors to be used in the design.

Requirements
Must have
• Must have
• * Call to action ad banners and Email creative.
• * Ad Banners in the 3 sizes noted in the project description.
• * Email creative must also be coded in responsive HTML.
• * The design must match the website https://harbor-lanternpage.com/
Nice to have
• Nice to have
• * Strong call to action
Should not have
• Should not have
• * Should not be cookie cutter. Stick to simple yet official looking.

```html
<!DOCTYPE html>
<html lang="en">
<head>
<meta charset="utf-8">
<title>Hernia Mesh Lawsuit Ad Banners</title>
<link rel="stylesheet" href="https://fonts.googleapis.com/css2?family=Montserrat:wght@700;800&family=Poppins:wght@500;600;700&family=Lora:wght@400&display=swap">
<style>
:root{
  --navy:#22345a;
  --navy-deep:#1c2a4a;
  --royal:#2f5fb8;
  --magenta:#c7326f;
  --plum:#7a3a6e;
  --sky:#3fa9f5;
  --tab-blue:#2f86f6;
  --cta-red:#ee1c24;
  --white:#ffffff;
  --label-red:#e8202a;
}
*{box-sizing:border-box;margin:0;padding:0}
html,body{width:1117px;height:1200px;overflow:hidden;background:var(--white)}
body{position:relative;font-family:"Montserrat",sans-serif;color:var(--white)}
.banner{position:absolute;overflow:hidden}
.photo{position:absolute;inset:0}
.banner > *:not(.photo){position:absolute;white-space:nowrap}
.kicker,.headline,.act-now{font-weight:800;line-height:1;transform-origin:left top}
.act-now{color:var(--sky)}
.body-copy{font-family:"Lora",serif;white-space:normal!important}
.promise{font-family:"Poppins",sans-serif;font-weight:500;line-height:1}
.cta{display:flex;background:var(--cta-red);text-decoration:none}
.cta-label{flex:1;display:flex;align-items:center;justify-content:center;font-family:"Poppins",sans-serif;font-weight:600;color:var(--white)}
.cta-arrow{background:var(--white);display:flex;align-items:center;justify-content:center}
.size-label{position:absolute;font-family:"Poppins",sans-serif;font-weight:500;color:var(--label-red);letter-spacing:3px;line-height:1}

/* 300x250 */
.rect{left:40px;top:41px;width:469px;height:391px}
.rect .photo{background:linear-gradient(120deg,var(--royal) 0%,#3a4fa0 45%,var(--plum) 70%,var(--magenta) 85%,#3b3f6e 100%)}
.rect .kicker{left:20px;top:8px;font-size:36px;transform:scaleX(.85)}
.rect .headline{left:20px;top:47px;font-size:56px;transform:scaleX(.8)}
.rect .body-copy{left:22px;top:112px;width:420px;font-size:19px;line-height:25px}
.rect .act-now{left:18px;top:222px;font-size:52px;transform:scaleX(.85)}
.rect .promise{left:23px;top:287px;font-size:18px;letter-spacing:1.6px}
.rect .cta{left:22px;top:324px;width:421px;height:55px}
.rect .cta-label{font-size:21px;letter-spacing:1.2px}
.rect .cta-arrow{width:70px}

/* 728x90 */
.leader{left:42px;top:585px;width:1009px;height:124px}
.leader .photo{background:linear-gradient(90deg,var(--navy) 0%,var(--navy) 38%,#34406a 62%,var(--plum) 85%,#b43c70 100%)}
.leader .kicker{left:11px;top:11px;font-size:23px;letter-spacing:2px}
.leader .headline{left:11px;top:42px;font-size:36px;letter-spacing:3px}
.leader .tab{left:0;top:81px;width:371px;height:43px;background:var(--tab-blue);border-top-right-radius:10px;display:flex;align-items:center;padding-left:14px;font-family:"Poppins",sans-serif;font-weight:500;font-size:16.5px}
.leader .body-copy{left:441px;top:10px;width:548px;font-size:17px;line-height:22px}
.leader .act-now{left:446px;top:77px;font-size:40px;transform:scaleX(.78)}
.leader .cta{left:631px;top:72px;width:366px;height:41px}
.leader .cta-label{font-size:19px;letter-spacing:3.4px}
.leader .cta-arrow{width:45px}

/* 320x50 */
.mobile{left:43px;top:837px;width:685px;height:106px}
.mobile .photo{background:linear-gradient(90deg,var(--navy-deep) 0%,var(--navy) 50%,#3a3f6a 75%,var(--plum) 92%,#b04070 100%)}
.mobile .kicker{left:12px;top:25px;font-size:19px;letter-spacing:1.8px}
.mobile .headline{left:12px;top:50px;font-size:37px;transform:scaleX(.87)}
.mobile .promise{left:333px;top:22px;font-size:15.5px;font-weight:600;letter-spacing:.6px}
.mobile .cta{left:330px;top:50px;width:340px;height:41px}
.mobile .cta-label{font-size:20px;font-weight:700;font-family:"Montserrat",sans-serif}
.mobile .cta-arrow{width:47px}
</style>
</head>
<body>

<section class="banner rect">
  <div class="photo" role="img" aria-label="Close-up of draped fabric in blue and magenta light"></div>
  <p class="kicker">INJURED FROM A HERNIA</p>
  <h2 class="headline">MESH SURGERY?</h2>
  <p class="body-copy">Have you had surgery using a surgical mesh, possibly for a hernia or a C-section? You may be eligible to join a surgical mesh class action lawsuit</p>
  <p class="act-now">ACT NOW</p>
  <p class="promise">FAST, FREE, NO OBLIGATION EVALUATION</p>
  <a class="cta">
    <span class="cta-label">FREE CASE EVALUATION</span>
    <span class="cta-arrow"><svg width="16" height="22" viewBox="0 0 16 22"><path d="M3 3l8 8-8 8" fill="none" stroke="#ee1c24" stroke-width="4"/></svg></span>
  </a>
</section>
<p class="size-label" style="left:57px;top:474px;font-size:28px">300-250</p>

<section class="banner leader">
  <div class="photo" role="img" aria-label="Draped fabric fading from navy to magenta"></div>
  <p class="kicker">INJURED FROM A HERNIA</p>
  <h2 class="headline">MESH SURGERY?</h2>
  <p class="tab">FAST, FREE, NO OBLIGATION EVALUATION</p>
  <p class="body-copy">Have you had surgery using a surgical mesh, possibly for a hernia or a C-section? You may be eligible to join a surgical mesh class action lawsuit</p>
  <p class="act-now">ACT NOW</p>
  <a class="cta">
    <span class="cta-label">FREE CASE EVALUATION</span>
    <span class="cta-arrow"><svg width="14" height="20" viewBox="0 0 14 20"><path d="M3 3l7 7-7 7" fill="none" stroke="#ee1c24" stroke-width="3.6"/></svg></span>
  </a>
</section>
<p class="size-label" style="left:42px;top:750px;font-size:23px">728-90</p>

<section class="banner mobile">
  <div class="photo" role="img" aria-label="Draped fabric fading from navy to magenta"></div>
  <p class="kicker">INJURED FROM A HERNIA</p>
  <h2 class="headline">MESH SURGERY?</h2>
  <p class="promise">FAST, FREE, NO OBLIGATION EVALUATION</p>
  <a class="cta">
    <span class="cta-label">FREE CASE EVALUATION</span>
    <span class="cta-arrow"><svg width="14" height="20" viewBox="0 0 14 20"><path d="M3 3l7 7-7 7" fill="none" stroke="#ee1c24" stroke-width="3.6"/></svg></span>
  </a>
</section>
<p class="size-label" style="left:42px;top:992px;font-size:35px">320-50</p>

<p class="size-label" style="left:58px;top:1111px;font-size:34px">ALL BANNERS</p>

</body>
</html>
```